A billboard for Pine Hollow Construction size 36.5’ x 14.5’

Hi guys. We are purchasing a billboard and are looking for a design (size 36.5’ x 14.5’). Our slogan is "Quality you deserve, service you can count on". The goal of this billboard is brand recognition primarily letting people know we do roofs. Attached are logos that can be used if needed. Not necessarily all of them need to be used.

Target Market(s)

Residents in the local areas needing or thinking about a roof replacement

Industry/Entity Type

Roofing

Requirements
Must have
• Logo and services (roof replacement, gutters, siding, and snow removal)
Nice to have
• take a look at our website for ideas www.pinehollowconstruction.example

```html
<!DOCTYPE html>
<html lang="en">
<head>
<meta charset="utf-8">
<title>Pine Hollow Construction – Billboard</title>
<link href="https://fonts.googleapis.com/css2?family=Saira:wght@600;700&display=swap" rel="stylesheet">
<style>
  :root {
    --page: #cccccc;
    --white: #ffffff;
    --red: #ee0909;
    --black: #0a0a0a;
    --badge-blue: #0a5f87;
    --badge-gray: #9a9a9a;
    --photo-top: #9c958a;
    --photo-bottom: #6e6a62;
  }
  html, body {
    margin: 0;
    padding: 0;
    width: 1200px;
    height: 875px;
    overflow: hidden;
    background: var(--page);
  }
  .billboard {
    position: absolute;
    left: 20px;
    top: 206px;
    width: 1160px;
    height: 463px;
    background: var(--white);
    overflow: hidden;
    font-family: "Saira", sans-serif;
  }
  .billboard__art {
    position: absolute;
    inset: 0;
  }
  .brand {
    position: absolute;
    left: 52px;
    top: 112px;
    display: flex;
    align-items: center;
    gap: 14px;
  }
  .brand__square {
    width: 46px;
    height: 46px;
    background: var(--red);
  }
  .brand__name {
    font-weight: 600;
    font-size: 34px;
    line-height: 36px;
    color: var(--black);
  }
  .slogan {
    position: absolute;
    left: 40px;
    width: 345px;
    top: 214px;
    margin: 0;
    text-align: center;
    font-weight: 600;
    font-size: 22px;
    line-height: 30px;
    color: var(--red);
  }
  .headline {
    position: absolute;
    left: 560px;
    width: 560px;
    top: 62px;
    margin: 0;
    text-align: center;
    color: var(--white);
    font-weight: 700;
    line-height: 1;
  }
  .headline__main {
    display: block;
    font-size: 70px;
    letter-spacing: 1px;
  }
  .headline__sub {
    display: block;
    font-size: 46px;
    margin-top: 2px;
  }
  .services {
    position: absolute;
    left: 560px;
    width: 560px;
    top: 180px;
    margin: 0;
    text-align: center;
    color: var(--white);
    font-weight: 600;
    font-size: 18px;
    line-height: 22px;
    letter-spacing: 0.5px;
  }
  .badge {
    position: absolute;
  }
  .badge--accredited {
    left: 98px; top: 311px; width: 131px; height: 49px;
    background: var(--badge-blue);
    border-radius: 3px;
  }
  .badge--shingles {
    left: 56px; top: 386px; width: 84px; height: 54px;
    background: var(--black);
  }
  .badge--pro {
    left: 198px; top: 386px; width: 60px; height: 54px;
    background: var(--badge-gray);
  }
</style>
</head>
<body>
  <main class="billboard">
    <svg class="billboard__art" width="1160" height="463" viewBox="0 0 1160 463">
      <defs>
        <linearGradient id="photo-tone" x1="0" y1="0" x2="0" y2="1">
          <stop offset="0" stop-color="var(--photo-top)"/>
          <stop offset="1" stop-color="var(--photo-bottom)"/>
        </linearGradient>
      </defs>
      <polygon class="red-field" points="526,0 1160,0 1160,463 268,463" fill="var(--red)"/>
      <polygon class="house-photo" role="img" aria-label="Photo of a brick house with a new grey shingle roof"
        points="410,212 1160,212 1160,463 300,463" fill="url(#photo-tone)"/>
      <polygon class="stripe stripe--long" points="549,0 572,0 312,463 286,463" fill="var(--black)"/>
      <polygon class="stripe stripe--short" points="494,178 523,178 361,463 332,463" fill="var(--black)"/>
    </svg>

    <div class="brand">
      <span class="brand__square"></span>
      <span class="brand__name">Pine Hollow<br>Construction</span>
    </div>

    <p class="slogan">Quality you deserve,<br>service you can count on</p>

    <div class="badge badge--accredited" aria-hidden="true"></div>
    <div class="badge badge--shingles" aria-hidden="true"></div>
    <div class="badge badge--pro" aria-hidden="true"></div>

    <h1 class="headline">
      <span class="headline__main">TRUSTWORTHY</span>
      <span class="headline__sub">ROOFING INSTALLATION</span>
    </h1>
    <p class="services">Roof Replacement &bull; Gutters &bull; Siding &bull; Snow Removal</p>
  </main>
</body>
</html>
```